Clearview Property Inspections

Property Inspection ( pre-purchase building inspections, swimming pool inspection, pest inspection , maintenance)

Industry/Entity Type

Building

Contact Information for Business Card

Tomas Varnell
info@clearviewinspect-demo.com.au
0412 867 219

ClearView Property Inspections
www.clearviewinspect-demo.com.au

on the back

Property Inspections
Property Maintenance

Safe Home....Safe Familu

```html
<!DOCTYPE html>
<html lang="en">
<head>
<meta charset="utf-8">
<title>ClearView Property Inspections – Business Card</title>
<link rel="stylesheet" href="https://fonts.googleapis.com/css2?family=Titillium+Web:wght@400;600;700&family=Kaushan+Script&display=swap">
<style>
  :root {
    --navy: #1f2a78;
    --navy-deep: #1c2570;
    --blue-glow: #1f74c6;
    --sky: #34a8e0;
    --ink: #2a2a2a;
    --white: #ffffff;
    --frame: #b9b9b9;
    --page: #ffffff;
  }
  * { margin: 0; padding: 0; box-sizing: border-box; }
  html, body {
    width: 972px;
    height: 1200px;
    overflow: hidden;
    background: var(--page);
    font-family: "Titillium Web", Arial, sans-serif;
  }
  .canvas { position: relative; width: 972px; height: 1200px; }

  .card {
    position: absolute;
    left: 12px;
    width: 950px;
    border: 1.5px solid var(--frame);
    overflow: hidden;
    background: var(--white);
  }
  .card--front { top: 12px; height: 586px; }
  .card--back { top: 608px; height: 588px; }

  .glow-band {
    position: absolute;
    left: 0; right: 0;
    background: radial-gradient(ellipse 55% 75% at 50% 50%, var(--blue-glow) 0%, #1c4fa6 45%, var(--navy-deep) 100%);
  }
  .card--front .glow-band { top: 0; height: 470px; }
  .card--back .glow-band { bottom: 0; height: 264px; }

  .brand-name {
    position: absolute;
    left: 0; right: 0;
    text-align: center;
    font-weight: 700;
    letter-spacing: 2px;
    line-height: 1;
  }
  .card--front .brand-name { top: 262px; font-size: 100px; color: var(--white); }
  .card--back .brand-name { top: 146px; font-size: 76px; color: var(--sky); }

  .services {
    position: absolute;
    left: 0; right: 0;
    text-align: center;
    font-weight: 600;
    letter-spacing: 0.3px;
    line-height: 1;
  }
  .card--front .services { top: 396px; font-size: 28px; color: var(--white); }
  .card--back .services { top: 257px; font-size: 27px; color: var(--navy); }

  .tagline {
    position: absolute;
    top: 492px;
    left: 0; right: 0;
    text-align: center;
    font-family: "Kaushan Script", cursive;
    font-size: 42px;
    color: var(--navy);
    line-height: 1.2;
  }

  .contact {
    position: absolute;
    left: 0; right: 0;
    bottom: 0;
    height: 264px;
    text-align: center;
    color: var(--white);
  }
  .contact-line {
    position: absolute;
    left: 0; right: 0;
    line-height: 1;
  }
  .contact-person { top: 30px; font-size: 40px; font-weight: 700; letter-spacing: 0.5px; }
  .contact-person .sep { margin: 0 18px; }
  .contact-email { top: 96px; font-size: 40px; font-weight: 400; }
  .contact-web { top: 158px; font-size: 40px; font-weight: 400; }
  .contact strong { font-weight: 700; }
</style>
</head>
<body>
<main class="canvas">

  <section class="card card--front" aria-label="Card front">
    <div class="glow-band"></div>
    <div class="brand-name">CLEARVIEW</div>
    <div class="services">PROPERTY INSPECTIONS &amp; MAINTENANCE</div>
    <div class="tagline">Clear View. . . , Sound Home</div>
  </section>

  <section class="card card--back" aria-label="Card back">
    <div class="brand-name">CLEARVIEW</div>
    <div class="services">PROPERTY INSPECTIONS &amp; MAINTENANCE</div>
    <div class="glow-band"></div>
    <div class="contact">
      <div class="contact-line contact-person">TOMAS VARNELL<span class="sep">•</span>0412 867 219</div>
      <div class="contact-line contact-email"><strong>info</strong>@clearviewinspect-demo.com.au</div>
      <div class="contact-line contact-web"><strong>www</strong>.clearviewinspect-demo.com.au</div>
    </div>
  </section>

</main>
</body>
</html>
```